Titlescreen rework for real estate homepage

Hello, this is my homepage (http://www.selbach-immobilien.de) and I am just looking for a title page for the title screen. So I guess the main target is finding a fitting picture for it. Re-arranging the menu is not a must, but I at the open everything even for new Ideas of additional elements. The rest of the homepage stays as it is. What I'm looking for is taff to describe, I already needed a long time finding the current picture. I am a real estate agent so it should have a link to estates. It could be a dark theme as it now or maybe something more light with "white" in it as you can scroll down. Of course it should work with the elements appearing bottom. Because I do not work in New York, just in a smaller area in Germany, no scyscrappers to find. I hope someone can show up with a new and fitting new title screen for me. I uploaded the logo-file for you to build in. The used font is raleway, cause its used in the logo as well. Its downloadable here: (https://www.glyphmeadow.com/fonts/raleway)
Target Market(s)
Real-Estate
Industry/Entity Type
Real Estate
Number of Pages Required
1 page
Look and feel
Each slider illustrates characteristics of the customer's brand and the style your logo design should communicate.

```html
<!DOCTYPE html>
<html lang="de">
<head>
<meta charset="utf-8">
<title>Selbach Immobilien</title>
<link href="https://fonts.googleapis.com/css2?family=Montserrat:wght@600;700;800&family=Raleway:wght@400;500;600;700&display=swap" rel="stylesheet">
<style>
:root{
  --navy:#2c4a8c;
  --blue:#3a5da8;
  --blue-deep:#24407c;
  --yellow:#f5c400;
  --ink:#1d1d1d;
  --text:#555;
  --white:#fff;
  --night:#0b0b10;
}
*{margin:0;padding:0;box-sizing:border-box}
html,body{width:1200px;height:3822px;overflow:hidden}
body{font-family:"Raleway",sans-serif;color:var(--ink);background:var(--white);position:relative}
.heading{font-family:"Montserrat",sans-serif}
section,header,footer{position:absolute;left:0;width:1200px}

/* nav */
.site-nav{top:0;height:76px;background:var(--navy);display:flex;align-items:center;padding:0 56px;z-index:3}
.brand{display:flex;align-items:center;gap:10px;color:var(--white);font-weight:700;font-size:24px;white-space:nowrap}
.brand-mark{width:18px;height:18px;background:var(--white)}
.menu{display:flex;margin-left:40px;list-style:none}
.menu li{font-size:12px;font-weight:600;letter-spacing:1px;color:#dfe6f5;padding:0 24px;height:76px;display:flex;align-items:center;white-space:nowrap}
.menu li.active{color:var(--white);border-top:3px solid var(--yellow);background:rgba(255,255,255,.08)}

/* hero */
.hero{top:76px;height:566px;background:
  linear-gradient(90deg,rgba(20,14,10,.75) 0%,rgba(20,14,10,.35) 40%,rgba(0,0,0,0) 65%),
  linear-gradient(180deg,#4d453b 0%,#5c574c 45%,#6b6350 70%,#2c2824 100%),
  linear-gradient(90deg,#3b2a1e 0%,#6a6358 40%,#8a8f78 70%,#4a4a42 100%)}
.hero::after{content:"";position:absolute;inset:0;background:linear-gradient(90deg,rgba(0,0,0,0) 0%,rgba(0,0,0,0) 60%,rgba(160,150,110,.35) 80%,rgba(0,0,0,.2) 100%)}
.hero-title{position:absolute;left:146px;top:216px;color:var(--white);z-index:1}
.hero-title h1{font-size:72px;line-height:66px;font-weight:800;letter-spacing:1px}
.hero-title p{font-size:13px;letter-spacing:1px;margin-top:10px}
.corner{position:absolute;width:36px;height:36px;border-color:var(--yellow);border-style:solid}
.corner.tl{left:-22px;top:-8px;border-width:8px 0 0 8px}
.corner.br{left:312px;top:98px;border-width:0 8px 8px 0}
.btn-start{position:absolute;left:150px;top:398px;width:164px;height:40px;background:#2b2b2b;color:var(--white);font-size:14px;display:flex;align-items:center;justify-content:center;z-index:1}

/* services grid */
.services{top:642px;height:721px}
.tile{position:absolute;width:600px;height:361px;color:var(--white);text-align:center;overflow:hidden}
.tile::before{content:"";position:absolute;inset:0;background:rgba(0,0,0,.22)}
.tile > *{position:relative}
.tile h3{font-size:17px;letter-spacing:1.5px;font-weight:700;margin-top:136px}
.tile p{font-size:13px;line-height:19px;width:330px;margin:14px auto 0;color:#f2f2f2}
.tile.sell{left:0;top:0;background:linear-gradient(180deg,#e6cf98 0%,#c99a2c 40%,#a87a24 75%,#7a5e3a 100%)}
.tile.buy{left:600px;top:0;background:linear-gradient(180deg,#d8d9dc 0%,#b9bbbf 45%,#9a9ca0 75%,#6d6f73 100%)}
.tile.docs{left:0;top:361px;background:linear-gradient(180deg,#a8a9a6 0%,#7d7d78 40%,#4b3c38 75%,#3a2526 100%)}
.tile.docs h3{margin-top:140px}
.tile.pool{left:600px;top:361px;background:var(--blue)}
.tile.pool::before{display:none}
.pool-card{position:absolute;left:88px;top:58px;width:500px;height:247px;background:var(--white);text-align:center;color:var(--ink)}
.pool-card h3{font-size:22px;color:var(--blue-deep);margin-top:56px;letter-spacing:2px;font-weight:600}
.pool-card p{font-size:13px;line-height:19px;color:var(--text);width:330px;margin:10px auto 0}
.btn-explore{display:inline-block;margin-top:18px;background:var(--yellow);color:var(--ink);font-family:"Montserrat",sans-serif;font-weight:700;font-size:13px;letter-spacing:1px;padding:14px 32px}

/* testimonial */
.testimonial{top:1363px;height:306px;text-align:center}
.testimonial h2{font-size:21px;letter-spacing:2px;color:var(--blue-deep);margin-top:44px;font-weight:700}
.testimonial p{font-size:13px;line-height:22px;color:var(--text);width:640px;margin:14px auto 0}
.testimonial .author{font-family:"Montserrat",sans-serif;color:var(--yellow);font-size:14px;font-weight:700;letter-spacing:1px;margin-top:20px}
.dots{display:flex;gap:12px;justify-content:center;margin-top:42px}
.dots span{width:11px;height:11px;border-radius:50%;background:#ddd}
.dots span.on{background:var(--yellow)}

/* properties */
.properties{top:1669px;height:395px}
.properties h2{text-align:center;font-size:22px;letter-spacing:2px;color:var(--blue-deep);margin-top:44px;font-weight:700}
.strip{position:absolute;top:115px;left:0;display:flex;width:1200px;height:280px}
.strip div{flex:1}
.p1{background:linear-gradient(180deg,#8fbbe2 0%,#c9a978 35%,#a77e52 60%,#4f7f34 100%)}
.p2{background:linear-gradient(180deg,#5f9fdd 0%,#9ec4e6 30%,#e8c548 55%,#4f8b30 100%)}
.p3{background:linear-gradient(180deg,#cfdceb 0%,#f3f2ee 40%,#d8d5cf 70%,#8a8580 100%)}
.p4{background:linear-gradient(180deg,#f0efec 0%,#d3d0cb 50%,#8d7b68 80%,#5c5048 100%)}
.p5{background:linear-gradient(180deg,#8fc0ea 0%,#dcdcd8 45%,#bdbdb8 65%,#4f7c36 100%)}

/* about */
.about{top:2064px;height:644px;background:
  linear-gradient(180deg,var(--night) 0%,#121218 45%,#2a2218 62%,#16161c 72%,var(--night) 100%)}
.portrait{position:absolute;right:0;top:200px;width:300px;height:444px;background:linear-gradient(180deg,#3c3f47 0%,#2a2d35 55%,#1b1e25 100%)}
.about-text{position:absolute;left:88px;top:112px;width:360px;color:var(--white)}
.about-text h2{font-size:19px;font-weight:700;letter-spacing:.5px}
.about-text p{font-size:14px;line-height:24px;margin-top:14px}
.about-text .name{font-weight:700;margin-top:24px;font-size:14px}
.about-text .role{margin-top:4px;font-size:14px}
.contact{list-style:none;margin-top:16px;font-size:13px;line-height:28px}
.contact li{display:flex;align-items:center;gap:12px}
.contact li.strong{font-weight:700}
.contact svg{width:13px;height:13px;fill:var(--white)}

/* features */
.features{top:2708px;height:446px}
.feature{position:absolute;top:88px;width:300px}
.feature:nth-child(1){left:88px}.feature:nth-child(2){left:428px}.feature:nth-child(3){left:768px}
.feature h3{font-size:17px;font-weight:500;letter-spacing:.5px}
.feature .sub{font-size:12px;color:var(--text);margin-top:4px}
.feature p{font-size:12px;line-height:19px;color:#777;margin-top:18px;height:168px}
.feature .link{display:flex;align-items:center;gap:12px;font-size:13px;font-weight:600;margin-top:12px}
.feature .link svg{width:18px;height:12px;stroke:var(--ink);fill:none;stroke-width:1.6}

/* info band */
.info{top:3154px;height:413px}
.info-panel{position:absolute;left:0;top:0;width:604px;height:413px;background:var(--blue);color:var(--white);padding:100px 0 0 116px}
.info-panel h2{font-size:24px;line-height:29px;letter-spacing:2px;font-weight:700}
.info-panel p{font-size:13px;line-height:19px;width:370px;margin-top:10px}
.info-buttons{display:flex;gap:20px;margin-top:20px}
.info-buttons span{border:2px solid var(--white);font-weight:700;font-size:14px;padding:7px 30px}
.info-photo{position:absolute;left:604px;top:0;width:596px;height:413px;background:linear-gradient(180deg,#8f8a84 0%,#d9d6d0 35%,#b8b2aa 60%,#2d2b2c 100%)}

/* subscribe */
.subscribe{top:3567px;height:196px}
.mailing{position:absolute;left:145px;top:62px}
.mailing h4,.social h4{font-size:13px;font-weight:500;letter-spacing:1.5px}
.mailing h4{margin-left:95px}
.form{display:flex;gap:10px;margin-top:26px}
.form .field{width:232px;height:30px;border:1px solid #aaa;font-size:11px;color:#999;padding:8px 10px}
.form .submit{width:92px;height:30px;background:#111;color:var(--white);font-size:12px;font-weight:700;display:flex;align-items:center;justify-content:center}
.social{position:absolute;left:708px;top:62px}
.icons{display:flex;gap:10px;margin-top:26px}
.icons span{width:28px;height:28px;border:2px solid #333;border-radius:50%}

.site-footer{top:3763px;height:59px;background:var(--navy);color:var(--white);font-size:12px;display:flex;align-items:center;justify-content:center}
</style>
</head>
<body>

<header class="site-nav">
  <div class="brand"><span class="brand-mark"></span>Selbach Immobilien</div>
  <ul class="menu">
    <li class="active">HOME</li><li>SELLING</li><li>PROPERTY</li><li>INFO</li><li>SERVICE</li><li>PARTNER</li><li>CONTACT</li>
  </ul>
</header>

<section class="hero" role="img" aria-label="Modern living room with leather chairs, bookshelf and a window view over open countryside">
  <div class="hero-title">
    <span class="corner tl"></span>
    <h1 class="heading">SELBACH REAL<br>ESTATE</h1>
    <p>YOUR MARKETER IN THE NORTH</p>
    <span class="corner br"></span>
  </div>
  <div class="btn-start">Get Started</div>
</section>

<section class="services">
  <div class="tile sell" role="img" aria-label="Bright living room with sofa and window blinds">
    <h3 class="heading">SELL PROPERTY</h3>
    <p>We sell your property at the best possible price. Find out more about our fair market valuation and a non-binding appraisal, tailored to your property.</p>
  </div>
  <div class="tile buy" role="img" aria-label="Modern white bathroom interior">
    <h3 class="heading">BUY PROPERTY</h3>
    <p>Take a look at our real estate portfolio and find your dream of a home. If there is nothing right for you, visit our service area for more.</p>
  </div>
  <div class="tile docs" role="img" aria-label="Living room with leather armchairs and a glass table">
    <h3 class="heading">DOCUMENTATION AND PROCESSING</h3>
    <p>We sell your property at the best possible price. Feel free to contact us for a fair market valuation and a non-binding appraisal of your home.</p>
  </div>
  <div class="tile pool">
    <div class="pool-card">
      <h3 class="heading">OWN POOL OF INTERESTED</h3>
      <p>Neque porro quisquam est qui dolorem ipsum quia dolor sit amet, consectetur, adipisci velit dolorem ipsum</p>
      <span class="btn-explore">EXPLORE NOW</span>
    </div>
  </div>
</section>

<section class="testimonial">
  <h2 class="heading">WHAT PEOPLE ARE SAYING</h2>
  <p>Lorem Ipsum is simply dummy text of the printing and typesetting industry. Lorem Ipsum has been the industry's standard dummy text ever since the 1500s, when an unknown printer took a galley of type and scrambled it to make a type specimen book.</p>
  <div class="author">LENA HOFF</div>
  <div class="dots"><span class="on"></span><span></span><span></span></div>
</section>

<section class="properties">
  <h2 class="heading">OUR PROPERTY</h2>
  <div class="strip">
    <div class="p1" role="img" aria-label="Brick townhouses on a green street"></div>
    <div class="p2" role="img" aria-label="Yellow detached house with lawn"></div>
    <div class="p3" role="img" aria-label="White new-build family house"></div>
    <div class="p4" role="img" aria-label="Bright empty interior with wooden floor"></div>
    <div class="p5" role="img" aria-label="White bungalow with garden"></div>
  </div>
</section>

<section class="about" role="img" aria-label="Harbour town skyline at night with lights reflected in the water">
  <div class="portrait" role="img" aria-label="Portrait of the company founder in a dark suit"></div>
  <div class="about-text">
    <h2>ÜBER SELBACH IMMOBILIEN</h2>
    <p>Selbach Immobilien hat sich auf den Verkauf und die Vermietung privater Wohnimmobilien im Radius von Neumünster über Kiel und Hamburg spezialisiert. Transparente Leistungen, individuelle Vermarktungsstrategien und die Nutzung moderner Vermarktungssysteme zeichnen uns aus.</p>
    <div class="name">Jonas Selbach</div>
    <div class="role">Firmengründer und Geschäftsführer</div>
    <ul class="contact">
      <li>Lindenweg 12, 24534 Neumünster</li>
      <li class="strong"><svg viewBox="0 0 16 16"><path d="M4 1l3 3-1.5 2a9 9 0 0 0 4.5 4.5L12 9l3 3-2 3C7 15 1 9 1 3z"/></svg>+49 170 5550 184</li>
      <li class="strong"><svg viewBox="0 0 16 16"><path d="M4 1l3 3-1.5 2a9 9 0 0 0 4.5 4.5L12 9l3 3-2 3C7 15 1 9 1 3z"/></svg>+49 4321 555 40 72</li>
      <li class="strong"><svg viewBox="0 0 16 16"><path d="M1 3h14v10H1z"/></svg>info@selbach-immo.de</li>
    </ul>
  </div>
</section>

<section class="features">
  <div class="feature">
    <h3>3D-BESICHTIGUNGEN</h3>
    <div class="sub">Innovative 3D Präsentation</div>
    <p>Als modernes Vermarktungsinstrument nutzen wir ein innovatives 3D-System. Besichtigungen können bei gleichzeitiger Beratung auf Wunsch online durchgeführt werden. Dies hat zahlreiche Vorteile für Kaufinteressenten und Immobilienbesitzer.</p>
    <div class="link"><svg viewBox="0 0 18 12"><path d="M0 6h16M11 1l5 5-5 5"/></svg>Informationen zur 3D-Besichtigung</div>
  </div>
  <div class="feature">
    <h3>FINANZIERUNG</h3>
    <div class="sub">Alles aus einer Hand</div>
    <p>Durch zusätzliche Qualifikation und leistungsstarke Partner ist es uns möglich, Sie als Kunde auch in allen Fragen der Finanzierung zu beraten. Ob allgemeiner Ratschlag oder vollständiges Finanzierungsangebot, sprechen Sie uns an.</p>
    <div class="link"><svg viewBox="0 0 18 12"><path d="M0 6h16M11 1l5 5-5 5"/></svg>Wissenswertes über die Finanzierung</div>
  </div>
  <div class="feature">
    <h3>IMMOCHECK &amp; KAUFGUTACHTEN</h3>
    <div class="sub">Kaufen, aber nicht um jeden Preis</div>
    <p>Sie möchten eine Immobilie von Privat oder bei einem anderen Makler erwerben und sind sich aber unsicher, ob der verlangte Kaufpreis gerechtfertigt ist? Wir unterstützen Sie als Fachmann bei der richtigen Entscheidung und begleiten Sie sogar zum Besichtigungstermin.</p>
    <div class="link"><svg viewBox="0 0 18 12"><path d="M0 6h16M11 1l5 5-5 5"/></svg>Ablauf Immocheck</div>
  </div>
</section>

<section class="info">
  <div class="info-panel">
    <h2 class="heading">WICHTIGE INFORMATIONEN FÜR<br>KÄUFER UND VERKÄUFER</h2>
    <p>Wir haben für Sie wichtige Informationen im Umgang mit Immobilien zusammengestellt. Denn, ob Verkauf oder Kauf, hier sollten Sie sich keine Fehler erlauben.</p>
    <div class="info-buttons"><span>Buyer</span><span>Seller</span></div>
  </div>
  <div class="info-photo" role="img" aria-label="Elegant bathroom with freestanding bathtub and chandelier"></div>
</section>

<section class="subscribe">
  <div class="mailing">
    <h4>SUBSCRIBE TO OUR MAILING LIST</h4>
    <div class="form"><div class="field">Email Address</div><div class="submit">SUBMIT</div></div>
  </div>
  <div class="social">
    <h4>JOIN US</h4>
    <div class="icons"><span></span><span></span><span></span><span></span></div>
  </div>
</section>

<footer class="site-footer">Copyright © info@selbach-immo.de</footer>

</body>
</html>
```